Famous Australian Web Brand (SiteKeyHub.com.au) Needs a New Website & Logo

SiteKeyHub.com.au is one of the leading domain name registration businesses in Australia and is looking for an overhaul of its website and brand.

SiteKeyHub.com.au current products/services include domain name registration, web hosting, web site creation and SSL certificates.

In this design contest on PixelSwarm, we would like designers to create a new logo and new website design for SiteKeyHub.com.au.

Here is what contest entrants will need to create:
- 1 new logo
- 1 new home page design
- 1 internal page (pricing page)

The winning designer will receive the main prize of $750. In addition to this, the winning designer will have the opportunity to work with SiteKeyHub for the build of the full website and may get ongoing design work from SiteKeyHub.
Updates

thank you all for your designs, we are after a web 2.0 look and feel, please dont use serif fonts, lets use modern and sleek ones, i will upload some samples of one we like shortly

header is to be in black with some texturing, white fonts and the call to action buttons are in green.

for the 6 free services, please use round edges for the images with the text under it, as i will upload shortly and we would like custome images, not stockimage types please

im uploading a sample of a background image for the header, which is black with texturing and also and image for the footer/middle of the page which has the correct shading of the grey for the middle section

please see file 8 for the look we are trying to get with our site and for font ideas

Reason: we have decided to extend the contest for another 3 days as a couple of designers have requested a bit more time

Target Market(s)

People that might need to buy a domain name or start a website: small business owners; entrepreneurs; bloggers; everyone from mum-and-dad website owners to tech savvy entrepreneurs. Geographically we will be targeting Australia but this should not influence the design.

Industry/Entity Type

Build

Requirements
Must have
• The logo should:
- Have the text "SiteKeyHub"
- Be positioned in the top left hand corner of the website
- Be either a wordmark, pictorial or abstract logo. That is, text-only logos are acceptable but we are also interested in receiving logos with a mark to the left that could somehow represents the business that we’re in

The homepage should:
- Feel modern, slick, web2.0
- Have a horizontal menu with 4 menu items: About Us | Contact Us | My Cart | Login
- Include the logo at the top
- Include the content from this Word Document
- Include the rough layout and style from this JPG template layout

The interior page should:
- Have the same look and feel as the home page
- Include the rough layout and style from this JPG attachment
- Include the content from this second Word Document
Nice to have
• - Grey, white and black primary colors
- Buttons that are green or lime green with a web2.0 call to action
- Full-width design (i.e. across the screen like PixelSwarm)
Should not have
• - Do not include overt Australian references. While we are an Australian business we do not want Australian flags, kangaroos or Captain Bellwether in our logo or on our website.
- Do not use the current red color scheme in the design. We want to move away from this.

```html
<!DOCTYPE html>
<html lang="en">
<head>
<meta charset="utf-8">
<title>SiteKeyHub – Domains, Hosting and More</title>
<link rel="stylesheet" href="https://fonts.googleapis.com/css2?family=Open+Sans:wght@400;600;700&display=swap">
<style>
:root{
  --page-bg:#ffffff;
  --brand:#4a80b4;
  --ink:#3a3a3a;
  --ink-soft:#555555;
  --nav-top:#3a3a3a;
  --nav-bottom:#0e0e0e;
  --nav-alt:#2c2c2c;
  --hero:#161616;
  --hero-line:#202020;
  --hero-mark:#3c3c3c;
  --field:#e2e2e2;
  --btn-dark:#3d3d3d;
  --btn-green-top:#9fd84a;
  --btn-green-bottom:#5d9e1c;
  --strip:#dcdcdc;
  --ribbon:#a9dbe8;
  --card:#f2f2f2;
  --frame:#bdbdbd;
  --footer:#5b5b5b;
  --footer-side:#4b4b4b;
  --footer-link:#8fd0ea;
  --accent-yellow:#f3ec9a;
  --white:#ffffff;
}
*{box-sizing:border-box;margin:0;padding:0}
html,body{width:1200px;height:1200px;overflow:hidden;background:var(--page-bg)}
body{font-family:"Open Sans",Arial,sans-serif;color:var(--ink)}
.page{position:relative;width:1020px;height:1020px;transform:scale(1.17647);transform-origin:0 0}
.abs{position:absolute}

.logo{left:46px;top:20px;display:flex;align-items:center;gap:8px}
.logo-dot{width:30px;height:30px;border-radius:50%;background:var(--brand)}
.logo-name{font-size:33px;font-weight:600;color:var(--brand);letter-spacing:-0.5px}

.account-tab{left:782px;top:0;width:196px;height:30px;background:linear-gradient(#4a4a4a,#111);border-radius:0 0 6px 6px;display:flex;align-items:center;justify-content:space-around;color:var(--white);font-size:14px}
.account-tab span{display:flex;align-items:center;gap:6px}
.header-phone{right:44px;top:40px;font-size:18px;font-weight:700;color:var(--ink);display:flex;align-items:center;gap:5px}

.main-nav{left:40px;top:71px;width:940px;height:37px;background:linear-gradient(var(--nav-top),var(--nav-bottom));border-radius:4px 4px 0 0;display:flex;overflow:hidden}
.main-nav a{color:var(--white);text-decoration:none;font-size:14px;display:flex;align-items:center;justify-content:center;border-right:1px solid #000;box-shadow:1px 0 0 #444}
.main-nav a.alt{background:var(--nav-alt);color:#e8e8e8;border-right:1px solid #111;box-shadow:none}

.hero{left:40px;top:108px;width:940px;height:199px;
  background:
    repeating-linear-gradient(45deg,transparent 0 3px,rgba(255,255,255,.025) 3px 4px),
    repeating-linear-gradient(-45deg,transparent 0 3px,rgba(0,0,0,.25) 3px 4px),
    linear-gradient(var(--hero-line),var(--hero));}
.hero-title{left:26px;top:15px;font-size:27px;font-weight:600;color:var(--white);letter-spacing:-0.3px;white-space:nowrap}
.hero-title mark{background:var(--hero-mark);color:var(--white);padding:0 2px}
.search-field{left:25px;top:73px;width:498px;height:40px;background:var(--field);border-radius:5px;border:1px solid #555}
.search-field .www{position:absolute;left:12px;top:2px;font-size:26px;font-weight:700;color:#444}
.search-field .tld{position:absolute;right:0;top:0;width:78px;height:38px;border-left:1px solid #aaa;display:flex;align-items:center;padding-left:10px;font-size:17px;color:#333}
.search-field .tld i{position:absolute;right:2px;top:3px;width:18px;height:32px;background:#8a8a8a;border-radius:3px;color:var(--white);font-style:normal;font-size:10px;display:flex;align-items:center;justify-content:center}
.btn-green{background:linear-gradient(var(--btn-green-top),var(--btn-green-bottom));color:var(--white);border-radius:5px;display:flex;align-items:center;justify-content:center;font-weight:600;border:1px solid #b9e67c}
.btn-search{left:533px;top:73px;width:92px;height:42px;font-size:22px}
.btn-dark{height:33px;top:145px;background:var(--btn-dark);color:var(--white);border-radius:4px;border:1px solid #222;box-shadow:inset 0 1px 0 #666;display:flex;align-items:center;justify-content:center;font-size:16px}
.hero-divider{left:670px;top:8px;width:1px;height:185px;background:#000;box-shadow:1px 0 0 #3a3a3a}
.price{left:712px;top:28px;color:var(--white);font-weight:600}
.price .amt{font-size:40px;line-height:1}
.price sup{font-size:20px;vertical-align:top}
.price small{font-size:22px}
.price-note{left:735px;top:86px;width:172px;font-size:14.5px;font-weight:700;color:var(--white);line-height:20px}
.btn-more{left:835px;top:159px;width:86px;height:31px;font-size:15px}

.video-strip{left:40px;top:307px;width:940px;height:148px;background:var(--strip)}
.video-card{top:8px;width:249px;height:90px;background:var(--white);border:4px solid var(--frame);display:flex;align-items:center;padding:4px}
.video-thumb{width:116px;height:74px;background:linear-gradient(90deg,#f3e6b8,#e9b86c 60%,#c6874d);position:relative}
.video-thumb svg{position:absolute;left:44px;top:22px}
.video-text{flex:1;text-align:center;color:#777;font-size:14.5px;line-height:20px}
.ribbon{left:30px;top:412px;width:860px;height:31px;background:var(--ribbon);display:flex;align-items:center;gap:8px;padding-left:14px;color:var(--white);font-size:17.5px;white-space:nowrap}

.feature{width:300px;height:205px;background:var(--card);padding:4px 12px}
.feature h2{font-size:18px;font-weight:600;color:var(--ink-soft);margin-bottom:4px;white-space:nowrap;letter-spacing:-0.2px}
.feature .media{width:274px;height:89px;border:3px solid var(--frame);border-radius:10px;margin-bottom:3px}
.feature p{font-size:10.4px;line-height:15px;color:#444;padding-right:4px}

.site-footer{left:0;top:900px;width:1020px;height:120px;background:var(--footer)}
.foot-col{top:8px;width:116px;font-family:Arial,sans-serif}
.foot-col h3{font-size:12px;font-weight:400;color:var(--footer-link);margin-bottom:3px}
.foot-col li{list-style:none;font-size:11px;color:var(--white);height:22px;line-height:20px;border-bottom:1px solid #8a8a8a}
.foot-col li:last-child{border-bottom:none}
.foot-contact{left:755px;top:0;width:265px;height:120px;background:var(--footer-side);border-left:1px solid #777;text-align:right;padding:12px 42px 0 0;color:var(--white)}
.foot-contact .ask{font-size:14px}
.foot-contact .big{font-size:28px;margin-top:2px}
.foot-contact .big em{font-style:normal;color:var(--accent-yellow)}
.foot-contact .tel{font-size:26px;color:var(--footer-link);display:flex;justify-content:flex-end;align-items:center;gap:6px}
</style>
</head>
<body>
<div class="page">

  <div class="abs logo"><span class="logo-dot"></span><span class="logo-name">SiteKeyHub</span></div>

  <div class="abs account-tab">
    <span><svg width="20" height="14" viewBox="0 0 20 14"><path d="M1 1h3l2 8h10l2-6H6" fill="none" stroke="#ddd" stroke-width="1.6"/><circle cx="8" cy="12" r="1.4" fill="#ddd"/><circle cx="15" cy="12" r="1.4" fill="#ddd"/></svg>My Cart</span>
    <span><svg width="12" height="16" viewBox="0 0 12 16"><circle cx="6" cy="4" r="3" fill="none" stroke="#ddd" stroke-width="1.6"/><path d="M6 7v8M6 11h3M6 14h3" stroke="#ddd" stroke-width="1.6"/></svg>Login</span>
  </div>
  <div class="abs header-phone"><svg width="12" height="16" viewBox="0 0 12 16"><path d="M3 1l3 3-2 2c1 2 2 4 4 5l2-2 2 3-2 2C5 14 1 8 1 3z" fill="#444"/></svg>1300 11 22 33</div>

  <nav class="abs main-nav">
    <a style="width:134px">DOMAINS&nbsp;▼</a>
    <a style="width:127px">CREATOR</a>
    <a style="width:122px">EMAIL</a>
    <a style="width:130px">HOSTING</a>
    <a style="width:157px">MARKETING</a>
    <a class="alt" style="width:125px">ABOUT US</a>
    <a class="alt" style="width:145px;border-right:none">CONTACT US</a>
  </nav>

  <section class="abs hero">
    <h1 class="abs hero-title">You get a lot <mark>more than</mark> just a <mark>domain name</mark></h1>
    <div class="abs search-field"><span class="www">www.</span><span class="tld">.com<i>▼</i></span></div>
    <div class="abs btn-green btn-search">Search</div>
    <div class="abs btn-dark" style="left:25px;width:146px">Renew a domain</div>
    <div class="abs btn-dark" style="left:199px;width:154px">Transfer a domain</div>
    <div class="abs btn-dark" style="left:384px;width:138px">View Price List</div>
    <div class="abs hero-divider"></div>
    <div class="abs price"><span class="amt"><sup>$</sup>11.99</span><small>/mo</small></div>
    <p class="abs price-note">Save 15% off all annual packages, only $119.99/pa</p>
    <div class="abs btn-green btn-more">See More</div>
  </section>

  <section class="abs video-strip">
    <div class="abs video-card" style="left:25px">
      <div class="video-thumb" role="img" aria-label="Video still: presenter beside the words why everyone needs a domain name"><svg width="26" height="26"><circle cx="13" cy="13" r="12" fill="#f08a1e"/><path d="M10 7l9 6-9 6z" fill="#fff"/></svg></div>
      <div class="video-text">Everyone needs<br>a domain name</div>
    </div>
    <div class="abs video-card" style="left:347px">
      <div class="video-thumb" role="img" aria-label="Video still: presenter beside the words why everyone needs a domain name"><svg width="26" height="26"><circle cx="13" cy="13" r="12" fill="#f08a1e"/><path d="M10 7l9 6-9 6z" fill="#fff"/></svg></div>
      <div class="video-text">Everyone needs<br>a domain name</div>
    </div>
    <div class="abs video-card" style="left:669px">
      <div class="video-thumb" role="img" aria-label="Video still: presenter beside the words why everyone needs a domain name"><svg width="26" height="26"><circle cx="13" cy="13" r="12" fill="#f08a1e"/><path d="M10 7l9 6-9 6z" fill="#fff"/></svg></div>
      <div class="video-text">Everyone needs<br>a domain name</div>
    </div>
  </section>
  <div class="abs ribbon"><svg width="12" height="14"><path d="M2 1l8 6-8 6" fill="none" stroke="#7a9aa5" stroke-width="2.5"/></svg>Everything your business needs to be successful online is FREE with every domain name.</div>

  <article class="abs feature" style="left:42px;top:463px">
    <h2>Free 15 Page Website</h2>
    <div class="media" role="img" aria-label="Screenshots of website templates" style="background:linear-gradient(90deg,#e9e6a0,#c8d86a 45%,#f3e27a 70%,#8cc4df)"></div>
    <p>Create a professional, full-featured website in minutes without any technical knowledge. Choose from 4,000+ stunning website designs and customize your site with near-limitless options. Upload your own artwork for a truly personalised look.</p>
  </article>
  <article class="abs feature" style="left:361px;top:463px">
    <h2>Free Professional Email</h2>
    <div class="media" role="img" aria-label="Envelope with an at sign" style="background:linear-gradient(135deg,#2a2a2a,#8a8a8a 40%,#e6e6e6 70%,#555)"></div>
    <p>Having a personalised address that matches your domain name (for example, Sam@SamsMuffins.com or Sales@SamsMuffins.com) gives your company a much more professional image when you communicate with customers and associates.</p>
  </article>
  <article class="abs feature" style="left:680px;top:463px">
    <h2>Free Website Hosting</h2>
    <div class="media" role="img" aria-label="Rack of web servers" style="background:linear-gradient(90deg,#1a1d24,#5a6270 50%,#20242c)"></div>
    <p>We provide the fast and secure hosting for your web-site. We take care of all the maintenance so all you have to do is create content for your site. Best of all, you don't have to pay a cent for hosting for as long as your domain is registered with us.</p>
  </article>

  <article class="abs feature" style="left:42px;top:684px">
    <h2>Free Search Engine Optimisation</h2>
    <div class="media" role="img" aria-label="Search engine cubes on a white floor" style="background:linear-gradient(90deg,#f4f4f4,#ffffff 50%,#d4d4d4)"></div>
    <p>What good is the best looking website if no one visits it? We thought about that too! All our sites are opti-mised for search engines by default to ensure that your website is found by Searchly and other search engines like Findora and Lookwise.</p>
  </article>
  <article class="abs feature" style="left:361px;top:684px">
    <h2>Free Business Class Support</h2>
    <div class="media" role="img" aria-label="Support agent wearing a headset" style="background:linear-gradient(90deg,#2f6fa8,#c9d7e4 45%,#d9a27c 75%,#b9b9b9)"></div>
    <p>This is a point of pride for us and we are here to help. We're available to you 24 hours a day, everyday. Many of our competitors don't even provide a phone number for you to call! You deserve the best, and we won't settle for providing anything less.</p>
  </article>
  <article class="abs feature" style="left:680px;top:684px">
    <h2>Guaranteed renewal price</h2>
    <div class="media" role="img" aria-label="Shadow of a dollar sign on a warm surface" style="background:radial-gradient(circle at 45% 50%,#5a3a1c,#b58446 55%,#e0b872)"></div>
    <p>You'll never pay more to renew your domain name than the rate you paid when you initially registered it, or what our registration rate was when you transferred. (The only exceptions would be if you took advantage of a limited-time, special price)</p>
  </article>

  <footer class="abs site-footer">
    <div class="abs foot-col" style="left:43px"><h3>Domains</h3><ul><li>Register Domains</li><li>Transfer Domains</li><li>Renew Domains</li><li>Name Servers</li></ul></div>
    <div class="abs foot-col" style="left:185px"><h3>Creator</h3><ul><li>Lorem Ipsum Text</li><li>Lorem Ipsum Text</li><li>Lorem Ipsum Text</li><li>Lorem Ipsum Text</li></ul></div>
    <div class="abs foot-col" style="left:329px"><h3>Email</h3><ul><li>Lorem Ipsum Text</li><li>Lorem Ipsum Text</li><li>Lorem Ipsum Text</li><li>Lorem Ipsum Text</li></ul></div>
    <div class="abs foot-col" style="left:474px"><h3>Hosting</h3><ul><li>Lorem Ipsum Text</li><li>Lorem Ipsum Text</li><li>Lorem Ipsum Text</li><li>Lorem Ipsum Text</li></ul></div>
    <div class="abs foot-col" style="left:618px"><h3>Marketing</h3><ul><li>Lorem Ipsum Text</li><li>Lorem Ipsum Text</li><li>Lorem Ipsum Text</li><li>Lorem Ipsum Text</li></ul></div>
    <div class="abs foot-contact">
      <div class="ask">HAVE A QUESTION FOR US?</div>
      <div class="big">CONTACT <em>US</em></div>
      <div class="tel"><svg width="14" height="18"><path d="M2 1l10 8-10 8" fill="none" stroke="#222" stroke-width="4"/></svg>1300 11 22 44</div>
    </div>
  </footer>

</div>
</body>
</html>
```